Digital ad to Parent Funnel

Those Puddle Jumpers works with preschoolers (also ages 2-8) doing hands-on activities that are Science Tech Engineering and Math (STEM) as a service business. The design is subtly colorful with the attached swatch definitions. Hexagons are a theme on the website.
www.thosepuddlejumpers.com
The purpose is on social media with a call to action to a landing page. I'd like placeholder text so I can be the copywriter. The banner I see is vertical, longer than wider. Design elements are welcoming, cheerful, and concrete. Pictures included are thematic for reference
https://www.pinterest.com/puddlejumpersKV/website-mood-board/
I'd like fonts that are more used than Dosis, which has a child-like font but doesn't render well online. Versatile design desired for deferring ad sizes, if possible. My laptop has InDesign.
Thanks!

```html
<!DOCTYPE html>
<html lang="en">
<head>
<meta charset="utf-8">
<title>Those Puddle Jumpers – STEM Ads</title>
<link href="https://fonts.googleapis.com/css2?family=Dosis:wght@300;400;600;700&display=swap" rel="stylesheet">
<style>
  :root {
    --page: #ffffff;
    --ad-bg: #f0e6dc;
    --purple: #5b2a8c;
    --green: #1f8a3a;
    --ink: #2b2b2b;
    --yellow: #f2ee2c;
  }
  * { margin: 0; padding: 0; box-sizing: border-box; }
  html, body { width: 1200px; height: 778px; overflow: hidden; background: var(--page); }
  body { position: relative; font-family: "Dosis", "Trebuchet MS", sans-serif; color: var(--ink); }

  .ad { position: absolute; background: var(--ad-bg); overflow: hidden; }
  .ad--tall { left: 29px; top: 32px; width: 397px; height: 705px; }
  .ad--wide { left: 462px; top: 200px; width: 706px; height: 368px; }

  .brand { position: absolute; display: flex; align-items: center; gap: 8px;
           font-weight: 700; color: var(--purple); white-space: nowrap; }
  .brand__dot { border-radius: 50%; background: var(--purple); flex: none; }

  .ad--tall .brand { left: 0; width: 100%; top: 62px; justify-content: center; font-size: 24px; }
  .ad--tall .brand__dot { width: 22px; height: 22px; }
  .ad--wide .brand { left: 41px; top: 274px; font-size: 16px; gap: 6px; }
  .ad--wide .brand__dot { width: 14px; height: 14px; }

  .photo { position: absolute; }
  .ad--tall .photo { left: 65px; top: 144px; width: 266px; height: 283px; }
  .ad--wide .photo { left: 429px; top: 40px; width: 300px; height: 340px; }

  .intro, .where { font-weight: 300; line-height: 0.98; }
  .stem { font-weight: 600; color: var(--purple); letter-spacing: 0.5px; line-height: 1.3; }
  .stem .bar { display: inline-block; width: 2px; height: 0.95em; background: var(--green);
               vertical-align: -0.1em; margin: 0 5px; }
  .phone { font-weight: 600; color: var(--purple); letter-spacing: 0.5px; }
  .phone .area { font-weight: 300; }
  .web { font-weight: 700; color: var(--purple); }

  .ad--tall .copy { position: absolute; left: 0; top: 452px; width: 100%; text-align: center; }
  .ad--tall .intro { font-size: 20px; }
  .ad--tall .stem { font-size: 27px; margin-top: 8px; }
  .ad--tall .where { font-size: 19px; margin-top: 6px; }
  .ad--tall .phone { font-size: 34px; margin-top: 12px; line-height: 1; }
  .ad--tall .web { font-size: 18px; margin-top: 2px; }

  .ad--wide .copy { position: absolute; left: 41px; top: 34px; width: 380px; }
  .ad--wide .intro { font-size: 19px; }
  .ad--wide .stem { font-size: 30px; margin-top: 10px; line-height: 1.3; }
  .ad--wide .where { font-size: 19px; margin-top: 10px; }
  .ad--wide .contact { position: absolute; left: 174px; top: 260px; }
  .ad--wide .phone { font-size: 33px; line-height: 1; }
  .ad--wide .web { font-size: 17px; margin-top: 2px; }
</style>
</head>
<body>

<section class="ad ad--tall">
  <div class="brand"><span class="brand__dot"></span>Those Puddle Jumpers</div>

  <svg class="photo" viewBox="0 0 266 283" role="img" aria-label="Photo of a smiling preschooler holding up a colorful pinwheel by a bright window">
    <defs>
      <linearGradient id="tall-photo" x1="0" y1="0" x2="1" y2="1">
        <stop offset="0" stop-color="#f4eef2"/>
        <stop offset="0.45" stop-color="#c9aab8"/>
        <stop offset="0.75" stop-color="#6b4a3e"/>
        <stop offset="1" stop-color="#1c2140"/>
      </linearGradient>
    </defs>
    <polygon points="133,5 240,50 262,150 215,262 95,278 8,222 8,75" fill="url(#tall-photo)" stroke="var(--yellow)" stroke-width="8" stroke-linejoin="round"/>
  </svg>

  <div class="copy">
    <p class="intro">Early Childhood Education experiences<br>with hands-on projects in</p>
    <p class="stem">SCIENCE<span class="bar"></span>TECHNOLOGY<br>ENGINEERING<span class="bar"></span>MATH</p>
    <p class="where">on site at preschooler's places of<br>care near Colorado Springs.</p>
    <p class="phone"><span class="area">(555)</span> 014-2290</p>
    <p class="web">www.thosepuddlejumpers.com</p>
  </div>
</section>

<section class="ad ad--wide">
  <div class="copy">
    <p class="intro">Early Childhood Education experiences<br>with hands-on projects in</p>
    <p class="stem">SCIENCE<span class="bar"></span>TECHNOLOGY<br>ENGINEERING<span class="bar"></span>MATH</p>
    <p class="where">on site at preschooler's places of<br>care near Colorado Springs.</p>
  </div>

  <div class="brand"><span class="brand__dot"></span>Those Puddle<br>Jumpers</div>

  <div class="contact">
    <p class="phone"><span class="area">(555)</span> 014-2290</p>
    <p class="web">www.thosepuddlejumpers.com</p>
  </div>

  <svg class="photo" viewBox="0 0 300 340" role="img" aria-label="Photo of a smiling preschooler holding up a colorful pinwheel by a bright window">
    <defs>
      <linearGradient id="wide-photo" x1="0" y1="0" x2="1" y2="1">
        <stop offset="0" stop-color="#f4eef2"/>
        <stop offset="0.45" stop-color="#c9aab8"/>
        <stop offset="0.75" stop-color="#6b4a3e"/>
        <stop offset="1" stop-color="#1c2140"/>
      </linearGradient>
    </defs>
    <polygon points="150,5 290,70 300,300 230,340 70,340 10,260 15,90" fill="url(#wide-photo)" stroke="var(--yellow)" stroke-width="8" stroke-linejoin="round"/>
  </svg>
</section>

</body>
</html>
```